BRIGHTVALE MENTORING powerpoint deck.

I REQUIRE A COMPANY POWERPOINT SLIDE DECK, WHICH MAY ALSO INCLUDE A NUMBER OF "MODELS". THIS MAY ALSO REQUIRE SOME FOLLOW UP WORK.

ATTACHED IS AN EXAMPLE SLIDE DECK FOR ONE OF MY CLIENTS. I would like to see a mock up of a few slides and then i can send a complete deck over.

Please note my website... www.brightvalementoring.co.uk

I LOOK FORWARD TO SEEING YOUR DESIGN.

THANK YOU,

OWEN.

Target Market(s)

I work in the "learning and development"/ education/ leadership/ coaching industry

Industry/Entity Type

Leadership

Font styles to use
Other font styles liked:
• century gothic

Requirements
Must have
• ideally there would be some alignment to my website. www.brightvalementoring.co.uk
• be fresh, clean, simple enough. look professional.
Nice to have
• how you present "models" i would come back for more work in the future if the work is good.
Should not have
• too brash.

```html
<!DOCTYPE html>
<html lang="en">
<head>
<meta charset="utf-8">
<title>Brightvale Mentoring – Slide Deck</title>
<link href="https://fonts.googleapis.com/css2?family=Lato:wght@300;400;700;900&display=swap" rel="stylesheet">
<style>
:root{
  --canvas:#efeff0;
  --teal:#129a8b;
  --teal-dark:#0f7f73;
  --teal-light:#6cbdb5;
  --teal-pale:#a9ddd6;
  --charcoal:#444849;
  --charcoal-dark:#333637;
  --slate:#627a79;
  --slate-light:#7f9190;
  --ink:#222;
  --grey-text:#6a6a6a;
  --white:#fff;
}
*{box-sizing:border-box;margin:0;padding:0}
html,body{width:1200px;height:1062px;overflow:hidden;background:var(--canvas)}
body{position:relative;font-family:'Lato',sans-serif;color:var(--ink)}
.slide{position:absolute;width:572px;height:323px;background:var(--white);overflow:hidden;box-shadow:0 1px 3px rgba(0,0,0,.18)}
.abs{position:absolute}
.page-num{position:absolute;right:0;bottom:0;width:26px;height:26px;background:var(--teal);color:#fff;font-size:12px;display:flex;align-items:center;justify-content:center}
.photo{position:absolute}
.light{font-weight:300}
.bold{font-weight:700}

/* slide 1 */
#cover{left:14px;top:26px}
#cover .edge{right:0;top:0;width:9px;height:100%;background:var(--charcoal-dark)}
#cover .brand{left:46px;top:42px;font-size:12px;letter-spacing:3px;color:var(--ink);display:flex;align-items:center;gap:6px}
#cover .brand i{width:10px;height:10px;border-radius:50%;background:var(--teal);display:block}
#cover .photo{left:0;top:70px;width:563px;height:155px;background:linear-gradient(180deg,#4a4d50 0%,#7b7e80 55%,#5d6062 100%)}
#cover .title-light{left:16px;top:146px;font-size:26px;font-weight:300;color:#fff;letter-spacing:.5px}
#cover .title-bold{left:16px;top:178px;font-size:28px;font-weight:900;color:#fff;letter-spacing:1px}
#cover .subtitle{left:19px;top:233px;font-size:11px;color:#444;letter-spacing:.6px}
#cover .presenter{left:19px;top:246px;font-size:8px;color:#777}
#cover .contact{left:19px;top:257px;font-size:6.5px;color:#555;line-height:13px}
#cover .contact div{display:flex;gap:38px}
#cover .intro{left:217px;top:242px;width:300px;font-size:7.5px;line-height:12px;color:#666}
#cover .social{left:0;bottom:0;display:flex}
#cover .social span{width:45px;height:35px;display:flex;align-items:center;justify-content:center}
#cover .social span:nth-child(1),#cover .social span:nth-child(2){background:var(--teal)}
#cover .social span:nth-child(3),#cover .social span:nth-child(4){background:var(--teal-light)}
#cover .social span i{display:block;width:12px;height:12px;border:2px solid #fff;border-radius:2px}
#cover .tint{right:9px;top:0;width:110px;height:100%;background:linear-gradient(90deg,rgba(230,243,241,0),rgba(230,243,241,.8))}

/* slide 2 */
#agenda{left:611px;top:26px}
#agenda .photo{left:0;top:0;width:260px;height:100%;background:linear-gradient(135deg,#0f7b70 0%,#2a9c8f 50%,#4fae9f 100%)}
#agenda .edge{left:0;top:0;width:9px;height:100%;background:var(--charcoal-dark)}
#agenda .band{left:260px;top:0;width:53px;height:100%;background:var(--teal-light)}
.time{position:absolute;right:327px;text-align:right;color:#fff}
.time b{font-size:11px;font-weight:400;letter-spacing:.3px}
.time b strong{font-weight:700}
.time small{display:block;font-size:6px;line-height:8px;margin-top:2px;opacity:.9}
.dot{position:absolute;left:272px;width:28px;height:28px;border-radius:50%;background:#fff;display:flex;align-items:center;justify-content:center}
.agenda-item{position:absolute;left:323px;color:var(--teal);font-size:11px;font-weight:700;letter-spacing:.4px}

/* slide 3 */
#section{left:14px;top:373px}
#section .dark{left:0;top:0;width:182px;height:190px;background:var(--charcoal-dark)}
#section .dark2{left:0;top:190px;width:182px;height:133px;background:var(--charcoal)}
#section .edge{left:0;top:0;width:9px;height:100%;background:#2a2c2d}
#section .photo{left:182px;top:0;width:390px;height:190px;background:linear-gradient(180deg,#8ea5a2 0%,#6f8885 55%,#58706d 100%)}
#section h2{position:absolute;left:21px;top:108px;color:#fff;font-size:20px;font-weight:300;line-height:24px;letter-spacing:.5px}
#section h2 strong{font-weight:700}
#section .sub-left{left:20px;top:212px;color:#fff;font-size:10px;font-weight:700;letter-spacing:1.3px}
#section .body-left{left:20px;top:232px;width:150px;color:#ddd;font-size:8.5px;line-height:16px}
#section .bar{left:217px;top:199px;width:208px;height:15px;background:var(--teal);color:#fff;font-size:10px;font-weight:700;letter-spacing:1.4px;padding-left:9px;line-height:15px}
.check{position:absolute;display:flex;gap:7px;font-size:5.5px;line-height:7px;color:#777;width:100px}
.check i{flex:none;width:10px;height:10px;border:1px solid #aaa;display:flex;align-items:center;justify-content:center}

/* slide 4 */
#model{left:611px;top:373px}
#model .rail{left:400px;top:0;width:43px;height:100%;background:var(--slate)}
#model .panel{left:443px;top:0;width:129px;height:100%;background:var(--charcoal)}
#model .ibox{position:absolute;left:400px;width:43px;height:51px;background:var(--slate-light);display:flex;align-items:center;justify-content:center}
#model .ibox i{width:28px;height:28px;border-radius:50%;background:#fff;display:flex;align-items:center;justify-content:center}
#model h3{position:absolute;left:454px;top:18px;color:#ddd;font-size:15px;font-weight:300;line-height:18px;letter-spacing:.3px}
#model h3 strong{font-weight:700;color:#eee}
#model .rule{left:454px;top:57px;width:107px;height:1px;background:#bbb}
.sub-h{position:absolute;left:460px;color:#fff;font-size:10.5px;letter-spacing:.5px}
.sub-h small{display:block;font-size:6px;line-height:8px;color:#ccc;margin-top:3px}
.tiny{position:absolute;font-size:4.5px;line-height:5.5px;color:#777;width:72px}

/* slide 5 */
#chart{left:14px;top:719px}
#chart .rail{left:0;top:0;width:43px;height:100%;background:var(--slate)}
#chart .tab{left:0;top:0;width:43px;height:42px;background:var(--charcoal);display:flex;align-items:center;justify-content:center}
#chart .side{left:376px;top:0;width:196px;height:100%;background:#f4f4f4;border-left:1px solid #ddd}
#chart h3{position:absolute;left:61px;top:21px;font-size:14.5px;font-weight:300;line-height:19px;color:#333}
#chart h3 strong{font-weight:700}
#chart .rule{left:61px;top:65px;width:107px;height:2px;background:var(--slate)}
#chart .caption{left:70px;top:247px;width:300px;font-size:8.5px;line-height:16px;color:#666}
#chart h4{position:absolute;left:403px;top:27px;font-size:20px;font-weight:300;line-height:22px;color:#777;letter-spacing:.6px}
#chart h4 strong{font-weight:700}
.step{position:absolute;left:399px;display:flex;align-items:center}
.step .n{font-size:26px;font-weight:300;color:var(--teal);width:36px}
.step .div{width:1px;height:26px;background:#444;margin-right:7px}
.step .t{font-size:6.5px;color:#444}
.step .t b{font-weight:900}
.step .t small{display:block;font-size:3.8px;line-height:4.5px;color:#666;margin-top:3px;width:110px}
#chart .side-body{left:403px;top:235px;width:150px;font-size:8.5px;line-height:16.5px;color:#777}

/* slide 6 */
#table{left:611px;top:719px}
#table .head{left:0;top:0;width:572px;height:66px;background:var(--teal)}
#table h3{position:absolute;left:15px;top:24px;font-size:21px;font-weight:300;color:#fff;letter-spacing:.6px}
#table h3 strong{font-weight:700}
.grid{position:absolute;left:0;top:66px;width:572px;border-collapse:collapse;font-size:10px}
.grid th,.grid td{padding:0}
.grid thead th{height:61px;color:#fff;font-weight:400;font-size:14px;vertical-align:top;padding-top:15px;position:relative}
.grid thead th.label{background:#1e1f20;text-align:left;padding:13px 0 0 36px;font-size:14px;line-height:17px;font-weight:300;width:180px}
.grid thead th.label strong{font-weight:700}
.grid thead th.c1{background:#646a6c;width:130px}
.grid thead th.c2{background:#7f8f8e;width:132px}
.grid thead th.c3{background:var(--teal-light)}
.grid thead th .base{position:absolute;left:0;bottom:0;width:100%;height:19px;background:rgba(0,0,0,.12)}
.grid thead th.c1 .base{background:#56595b}
.grid thead th.c2 .base{background:#6e7d7c}
.grid thead th.c3 .base{background:#47a69c}
.grid tbody td{height:31px;color:#666;text-align:center}
.grid tbody td:first-child{text-align:left;padding-left:36px;color:#444;vertical-align:top;padding-top:7px}
.grid tbody tr:nth-child(odd) td{background:#f6f6f6}
.grid tbody tr:nth-child(even) td{background:#eaeaea}
.grid tfoot td{height:41px;color:#fff;font-size:14px;text-align:center}
.grid tfoot td:first-child{background:#1e1f20}
.grid tfoot td.c1{background:#646a6c}
.grid tfoot td.c2{background:#7f8f8e}
.grid tfoot td.c3{background:var(--teal-light)}
</style>
</head>
<body>

<!-- Cover -->
<section class="slide" id="cover">
  <div class="abs tint"></div>
  <div class="abs brand"><i></i><span>BRIGHTVALE</span></div>
  <div class="photo" role="img" aria-label="Black and white city skyline with a suspension bridge"></div>
  <div class="abs title-light">BRIGHTVALE</div>
  <div class="abs title-bold">MENTORING</div>
  <div class="abs subtitle">Subtitle Goes Here</div>
  <div class="abs presenter">Presented by : Clara Fenwick</div>
  <div class="abs contact">
    <div><span>&#9990;</span><span>1-555-0193</span></div>
    <div><span>&#9993;</span><span>clara.fenwick@brightvale.example</span></div>
  </div>
  <p class="abs intro">Lorem ipsum dolor sit amet, ligula suspendisse nulla pretium, rhoncus tempor fermentum, enim integer ad vestibulum volutpat. Nisl rhoncus turpis est, vel elit, congue wisi enim nunc ultricies sit, magna tincidunt.</p>
  <div class="abs social">
    <span><svg width="16" height="16" viewBox="0 0 16 16" fill="none" stroke="#fff" stroke-width="1.2"><circle cx="8" cy="8" r="7"/><ellipse cx="8" cy="8" rx="3" ry="7"/><line x1="1" y1="8" x2="15" y2="8"/></svg></span>
    <span><i></i></span><span><i></i></span><span><i></i></span>
  </div>
  <div class="abs edge"></div>
</section>

<!-- Agenda -->
<section class="slide" id="agenda">
  <div class="photo" role="img" aria-label="Teal-tinted photo of hands typing on a laptop"></div>
  <div class="abs edge"></div>
  <div class="abs band"></div>
  <div class="time" style="top:41px"><b>08.00 - <strong>09.00</strong> AM</b><small>Lorem Ipsum Dolor<br>Sit Amet</small></div>
  <div class="time" style="top:99px"><b>10.00 - <strong>11.00</strong> AM</b><small>Lorem Ipsum Dolor<br>Sit Amet</small></div>
  <div class="time" style="top:157px"><b>13.00 - <strong>14.00</strong> AM</b><small>Lorem Ipsum Dolor<br>Sit Amet</small></div>
  <div class="time" style="top:215px"><b>15.00 -16.00 AM</b><small>Lorem Ipsum Dolor<br>Sit Amet</small></div>
  <div class="time" style="top:273px"><b>17.00 - <strong>18.00</strong> AM</b><small>Lorem Ipsum Dolor<br>Sit Amet</small></div>
  <div class="dot" style="top:31px"><svg width="12" height="12" viewBox="0 0 12 12" fill="none" stroke="#9ccfc9"><path d="M2 10 L3 7 L8 2 L10 4 L5 9 Z"/></svg></div>
  <div class="dot" style="top:90px"><svg width="12" height="12" viewBox="0 0 12 12" fill="none" stroke="#9ccfc9"><rect x="3" y="1.5" width="6" height="9"/><line x1="4.5" y1="5" x2="7.5" y2="5"/><line x1="4.5" y1="7" x2="7.5" y2="7"/></svg></div>
  <div class="dot" style="top:148px"><svg width="12" height="12" viewBox="0 0 12 12" fill="none" stroke="#9ccfc9"><circle cx="6" cy="6" r="4.5"/><circle cx="6" cy="6" r="1.8"/></svg></div>
  <div class="dot" style="top:208px"><svg width="12" height="12" viewBox="0 0 12 12" fill="none" stroke="#9ccfc9"><path d="M1.5 3 H5 L6 4 H10.5 V9.5 H1.5 Z"/></svg></div>
  <div class="dot" style="top:265px"><svg width="12" height="12" viewBox="0 0 12 12" fill="none" stroke="#9ccfc9"><path d="M6 2 L10.5 4.5 L6 7 L1.5 4.5 Z"/><path d="M1.5 7 L6 9.5 L10.5 7"/></svg></div>
  <div class="agenda-item" style="top:47px">Review of 2016</div>
  <div class="agenda-item" style="top:106px">Look ahead to 2017- 2019</div>
  <div class="agenda-item" style="top:165px">CSR programme</div>
  <div class="agenda-item" style="top:224px">Next steps</div>
  <div class="agenda-item" style="top:283px">Lorem Ipsum</div>
  <div class="page-num">2</div>
</section>

<!-- Section divider -->
<section class="slide" id="section">
  <div class="abs dark"></div>
  <div class="abs dark2"></div>
  <div class="abs edge"></div>
  <svg class="abs" style="left:48px;top:26px" width="70" height="58" viewBox="0 0 70 58" fill="none" stroke="#fff" stroke-width="2.2"><path d="M2 54 V4 H22 L28 10 H60 V20"/><path d="M8 20 V12 H54 V20"/><path d="M2 54 L12 22 H67 L58 54 Z"/></svg>
  <h2>PLACE YOUR<br><strong>HEADER HERE</strong></h2>
  <div class="photo" role="img" aria-label="Grey-green city skyline with a suspension bridge"></div>
  <div class="abs sub-left">SUBTITLE GOES HERE</div>
  <p class="abs body-left">Lorem ipsum dolor sit amet, ligula suspendisse nulla pretium, rhoncus tempor fermentum, enim integer ad vestibulum volutpat.</p>
  <div class="abs bar">SUBTITLE GOES HERE</div>

  <div class="check" style="left:226px;top:227px"><i></i><span>Lorem Ipsum Dolor Sit<br>Amet</span></div>
  <div class="check" style="left:226px;top:246px"><i></i><span>Lorem Ipsum Dolor Sit<br>Amet</span></div>
  <div class="check" style="left:226px;top:264px"><i></i><span>Lorem Ipsum Dolor Sit<br>Amet</span></div>
  <div class="check" style="left:226px;top:283px"><i></i><span>Lorem Ipsum Dolor Sit<br>Amet</span></div>
  <div class="check" style="left:340px;top:227px"><i></i><span>Lorem Ipsum Dolor Sit<br>Amet</span></div>
  <div class="check" style="left:340px;top:246px"><i></i><span>Lorem Ipsum Dolor Sit<br>Amet</span></div>
  <div class="check" style="left:340px;top:264px"><i></i><span>Lorem Ipsum Dolor Sit<br>Amet</span></div>
  <div class="check" style="left:340px;top:283px"><i></i><span>Lorem Ipsum Dolor Sit<br>Amet</span></div>
  <div class="check" style="left:455px;top:227px"><i></i><span>Lorem Ipsum Dolor Sit<br>Amet</span></div>
  <div class="check" style="left:455px;top:246px"><i></i><span>Lorem Ipsum Dolor Sit<br>Amet</span></div>
  <div class="check" style="left:455px;top:264px"><i></i><span>Lorem Ipsum Dolor Sit<br>Amet</span></div>
  <div class="check" style="left:455px;top:283px"><i></i><span>Lorem Ipsum Dolor Sit<br>Amet</span></div>
  <div class="page-num">3</div>
</section>

<!-- Cycle model -->
<section class="slide" id="model">
  <svg class="abs" style="left:0;top:0" width="400" height="323" viewBox="0 0 400 323">
    <g fill="none" stroke-width="11">
      <circle cx="200" cy="155" r="64" stroke="var(--teal)" stroke-dasharray="36 366" transform="rotate(-115 200 155)"/>
      <circle cx="200" cy="155" r="64" stroke="#4a4e58" stroke-dasharray="36 366" transform="rotate(-70 200 155)"/>
      <circle cx="200" cy="155" r="64" stroke="var(--teal-pale)" stroke-dasharray="36 366" transform="rotate(-25 200 155)"/>
      <circle cx="200" cy="155" r="64" stroke="var(--slate)" stroke-dasharray="36 366" transform="rotate(20 200 155)"/>
      <circle cx="200" cy="155" r="64" stroke="var(--teal-light)" stroke-dasharray="36 366" transform="rotate(65 200 155)"/>
      <circle cx="200" cy="155" r="64" stroke="#4a4e58" stroke-dasharray="36 366" transform="rotate(110 200 155)"/>
      <circle cx="200" cy="155" r="64" stroke="var(--teal-pale)" stroke-dasharray="36 366" transform="rotate(155 200 155)"/>
      <circle cx="200" cy="155" r="64" stroke="var(--slate)" stroke-dasharray="36 366" transform="rotate(200 200 155)"/>
    </g>
    <g fill="none" stroke="#444" stroke-width="1">
      <polyline points="193,78 193,58"/>
      <polyline points="248,108 264,82 286,82"/>
      <polyline points="265,135 272,135"/>
      <polyline points="252,210 268,225 283,225"/>
      <polyline points="207,229 207,248"/>
      <polyline points="153,208 139,223 118,223"/>
      <polyline points="136,155 120,155"/>
      <polyline points="152,108 133,85 105,85"/>
    </g>
    <g fill="var(--teal)">
      <rect x="189" y="30" width="8" height="14" rx="3"/>
      <circle cx="103" cy="101" r="8" fill="none" stroke="#444"/>
      <text x="103" y="104" font-size="9" text-anchor="middle" fill="#444" font-family="Lato,sans-serif">$</text>
      <rect x="303" y="88" width="16" height="11" fill="none" stroke="#444"/>
      <circle cx="311" cy="145" r="7" fill="var(--teal-light)"/>
      <rect x="314" y="222" width="14" height="9" fill="#444"/>
      <circle cx="206" cy="253" r="3"/><circle cx="199" cy="259" r="3"/><circle cx="213" cy="259" r="3"/>
      <circle cx="115" cy="237" r="6" fill="#333"/>
      <rect x="108" y="148" width="11" height="11" fill="var(--teal-pale)"/>
    </g>
    <text x="200" y="153" text-anchor="middle" font-family="Lato,sans-serif" font-size="10" fill="#333">PLACE YOUR</text>
    <text x="200" y="166" text-anchor="middle" font-family="Lato,sans-serif" font-size="10" font-weight="700" fill="#333">HEADER</text>
  </svg>
  <div class="tiny" style="left:160px;top:16px;text-align:center">Lorem ipsum dolor sit amet, consectetur adipiscing elit, sed</div>
  <div class="tiny" style="left:263px;top:66px">Lorem ipsum dolor sit amet, consectetur adipiscing elit, sed</div>
  <div class="tiny" style="left:296px;top:158px">Lorem ipsum dolor sit amet, consectetur adipiscing elit, sed</div>
  <div class="tiny" style="left:247px;top:221px">Lorem ipsum dolor sit amet, consectetur adipiscing elit, sed</div>
  <div class="tiny" style="left:184px;top:270px;text-align:center">Lorem ipsum dolor sit amet, consectetur adipiscing elit, sed</div>
  <div class="tiny" style="left:101px;top:240px">Lorem ipsum dolor sit amet, consectetur adipiscing elit, sed</div>
  <div class="tiny" style="left:40px;top:168px">Lorem ipsum dolor sit amet, consectetur adipiscing elit, sed</div>
  <div class="tiny" style="left:68px;top:76px">Lorem ipsum dolor sit amet, consectetur adipiscing elit, sed</div>
  <div class="abs rail"></div>
  <div class="abs panel"></div>
  <div class="ibox" style="top:82px"><i><svg width="12" height="12" viewBox="0 0 12 12" fill="none" stroke="#666"><path d="M2 10 L3 7 L8 2 L10 4 L5 9 Z"/></svg></i></div>
  <div class="ibox" style="top:136px"><i><svg width="12" height="12" viewBox="0 0 12 12" fill="none" stroke="#666"><rect x="3" y="1.5" width="6" height="9"/><line x1="4.5" y1="5" x2="7.5" y2="5"/></svg></i></div>
  <div class="ibox" style="top:190px"><i><svg width="12" height="12" viewBox="0 0 12 12" fill="none" stroke="#666"><circle cx="6" cy="6" r="4.5"/><circle cx="6" cy="6" r="1.8"/></svg></i></div>
  <h3>PLACE YOUR<br><strong>HEADER HERE</strong></h3>
  <div class="abs rule"></div>
  <div class="sub-h" style="top:93px">Sub Header<small>Lorem Ipsum Dolor<br>Sit Amet</small></div>
  <div class="sub-h" style="top:148px">Sub Header<small>Lorem Ipsum Dolor<br>Sit Amet</small></div>
  <div class="sub-h" style="top:204px">Sub Header<small>Lorem Ipsum Dolor<br>Sit Amet</small></div>
  <div class="page-num">4</div>
</section>

<!-- Chart -->
<section class="slide" id="chart">
  <div class="abs rail"></div>
  <div class="abs tab"><svg width="20" height="16" viewBox="0 0 20 16" fill="none" stroke="#ccc"><path d="M1 15 V1 H7 L9 3 H19 V15 Z"/><line x1="6" y1="9" x2="14" y2="9"/><line x1="6" y1="12" x2="14" y2="12"/></svg></div>
  <h3>PLACE YOUR<br><strong>HEADER HERE</strong></h3>
  <div class="abs rule"></div>
  <svg class="abs" style="left:62px;top:98px" width="308" height="120" viewBox="0 0 308 120" font-family="Lato,sans-serif">
    <g fill="#999" font-size="3.5">
      <circle cx="238" cy="8" r="1.8" fill="var(--teal-light)"/><text x="242" y="9.2">Receipts</text>
      <circle cx="260" cy="8" r="1.8" fill="var(--slate)"/><text x="264" y="9.2">Sales</text>
      <circle cx="281" cy="8" r="1.8" fill="var(--charcoal)"/><text x="285" y="9.2">Orders</text>
    </g>
    <g stroke="#e6e6e6" stroke-width=".6">
      <line x1="8" y1="16" x2="306" y2="16"/><line x1="8" y1="26.2" x2="306" y2="26.2"/><line x1="8" y1="36.4" x2="306" y2="36.4"/><line x1="8" y1="46.6" x2="306" y2="46.6"/><line x1="8" y1="56.8" x2="306" y2="56.8"/><line x1="8" y1="67" x2="306" y2="67"/><line x1="8" y1="77.2" x2="306" y2="77.2"/><line x1="8" y1="87.4" x2="306" y2="87.4"/><line x1="8" y1="97.6" x2="306" y2="97.6"/><line x1="8" y1="107.8" x2="306" y2="107.8"/>
    </g>
    <line x1="8" y1="118" x2="306" y2="118" stroke="#bbb" stroke-width=".6"/>
    <g font-size="3.2" fill="#666" text-anchor="end">
      <text x="6" y="17">100</text><text x="6" y="27">90</text><text x="6" y="37">80</text><text x="6" y="47">70</text><text x="6" y="57">60</text><text x="6" y="68">50</text><text x="6" y="78">40</text><text x="6" y="88">30</text><text x="6" y="98">20</text><text x="6" y="108">10</text><text x="6" y="119">0</text>
    </g>
    <rect x="16" y="87" width="15" height="31" fill="var(--teal-light)"/>
    <rect x="34" y="26" width="15" height="92" fill="var(--slate)"/>
    <rect x="52" y="57" width="15" height="61" fill="var(--charcoal)"/>
    <rect x="110" y="16" width="15" height="102" fill="var(--teal-light)"/>
    <rect x="128" y="36" width="15" height="82" fill="var(--slate)"/>
    <rect x="146" y="90" width="15" height="28" fill="var(--charcoal)"/>
    <rect x="204" y="36" width="15" height="82" fill="var(--teal-light)"/>
    <rect x="222" y="26" width="15" height="92" fill="var(--slate)"/>
    <rect x="240" y="67" width="15" height="51" fill="#b5b8b9"/>
    <rect x="298" y="47" width="0" height="0"/>
    <rect x="252" y="0" width="0" height="0"/>
    <rect x="256" y="0" width="0" height="0"/>
    <rect x="262" y="0" width="0" height="0"/>
    <g transform="translate(-24 0)">
      <rect x="298" y="46" width="15" height="72" fill="var(--teal-light)"/>
      <rect x="316" y="36" width="15" height="82" fill="var(--slate)"/>
    </g>
    <rect x="292" y="77" width="14" height="41" fill="var(--charcoal)"/>
    <g font-size="3.5" font-weight="700" fill="#333" text-anchor="middle">
      <text x="41" y="124">2013</text><text x="135" y="124">2014</text><text x="229" y="124">2015</text><text x="290" y="124">2016</text>
    </g>
  </svg>
  <p class="abs caption">Lorem ipsum dolor sit amet, ligula suspendisse nulla pretium, rhoncus tempor fermentum, enim integer ad vestibulum volutpat.</p>
  <div class="abs side"></div>
  <h4>PLACE YOUR<br><strong>HEADER HERE</strong></h4>
  <div class="step" style="top:104px"><span class="n">01</span><span class="div"></span><span class="t"><b>INFOGRAPHIC</b> YOUR TEXT<small>Lorem ipsum dolor sit amet, consectetur adipiscing elit sed do.</small></span></div>
  <div class="step" style="top:146px"><span class="n">02</span><span class="div"></span><span class="t"><b>INFOGRAPHIC</b> YOUR TEXT<small>Lorem ipsum dolor sit amet, consectetur adipiscing elit sed do.</small></span></div>
  <div class="step" style="top:188px"><span class="n">03</span><span class="div"></span><span class="t"><b>INFOGRAPHIC</b> YOUR TEXT<small>Lorem ipsum dolor sit amet, consectetur adipiscing elit sed do.</small></span></div>
  <p class="abs side-body">Lorem ipsum dolor sit amet, ligula suspendisse nulla pretium, rhoncus tempor fermentum, enim integer ad vestibulum volutpat.</p>
  <div class="page-num">5</div>
</section>

<!-- Table -->
<section class="slide" id="table">
  <div class="abs head"></div>
  <h3>PLACE YOUR <strong>HEADER HERE</strong></h3>
  <table class="grid">
    <thead>
      <tr>
        <th class="label">PLACE YOUR<br><strong>HEADER HERE</strong></th>
        <th class="c1">Value<span class="base"></span></th>
        <th class="c2">Value<span class="base"></span></th>
        <th class="c3">Value<span class="base"></span></th>
      </tr>
    </thead>
    <tbody>
      <tr><td>Lorem ipsum dolor sit amet</td><td>3455634</td><td>3455634</td><td>3455634</td></tr>
      <tr><td>Lorem ipsum dolor sit amet</td><td>45645</td><td>45645</td><td>45645</td></tr>
      <tr><td>Lorem ipsum dolor sit amet</td><td>46758768</td><td>46758768</td><td>46758768</td></tr>
      <tr><td>Lorem ipsum dolor sit amet</td><td>3454654</td><td>3454654</td><td>3454654</td></tr>
      <tr><td>Lorem ipsum dolor sit amet</td><td>78976890</td><td>78976890</td><td>78976890</td></tr>
    </tbody>
    <tfoot>
      <tr><td></td><td class="c1">$ 78,976,890</td><td class="c2">$ 78,976,890</td><td class="c3">$ 78,976,890</td></tr>
    </tfoot>
  </table>
</section>

</body>
</html>
```